Craft Harbor(PowerPoint Template)
Craft Harbor
Creating Leaders Within
Business focus on 4 key areas:
1. Skills Training.
2. Leadership Training
3. Consultancy
4. Coaching
Consulting
Corporate. To be used in mainly for training purposes. Secondary use for Presentation.
I would like clean and bright background so fonts can be visible. Please be creative.
Ai file for Logo

```html
<!DOCTYPE html>
<html lang="en">
<head>
<meta charset="utf-8">
<title>Craft Harbor — Presentation Template</title>
<link href="https://fonts.googleapis.com/css2?family=Open+Sans:ital,wght@0,400;0,600;0,700;0,800;1,700;1,800&display=swap" rel="stylesheet">
<style>
  :root {
    --red: #c8102e;
    --red-dark: #9e0b22;
    --blue: #1b75bb;
    --yellow: #f2b705;
    --ink: #333333;
    --muted: #6b6b6b;
    --rule: #d9d9d9;
    --paper: #ffffff;
    --stage: #ecebe8;
  }
  * { box-sizing: border-box; margin: 0; padding: 0; }
  html, body { width: 1200px; height: 646px; overflow: hidden; }
  body {
    background: var(--stage);
    font-family: "Open Sans", Arial, sans-serif;
    color: var(--ink);
    position: relative;
  }
  .slide {
    position: absolute;
    width: 360px; height: 270px;
    background: var(--paper);
    box-shadow: 0 2px 8px rgba(0,0,0,.18);
    overflow: hidden;
  }
  .row-1 { top: 36px; } .row-2 { top: 340px; }
  .col-1 { left: 30px; } .col-2 { left: 420px; } .col-3 { left: 810px; }

  /* brand lockup */
  .brand { display: flex; align-items: center; gap: 6px; }
  .brand-mark { width: 14px; height: 14px; background: var(--red); }
  .brand-name { font-weight: 800; color: var(--ink); font-size: 13px; letter-spacing: -.2px; white-space: nowrap; }
  .brand.small .brand-mark { width: 9px; height: 9px; }
  .brand.small .brand-name { font-size: 9px; }

  /* header of content slides */
  .slide-head { position: absolute; left: 14px; right: 14px; top: 12px; height: 22px;
    display: flex; justify-content: space-between; align-items: center;
    border-bottom: 1.5px solid var(--red); padding-bottom: 4px; }
  .slide-title { font-size: 11px; font-weight: 800; font-style: italic; color: var(--red); text-transform: uppercase; }
  .sub { font-size: 7.5px; font-weight: 700; font-style: italic; color: var(--blue); margin-bottom: 3px; }
  .body { font-size: 6.5px; line-height: 1.45; color: var(--muted); }
  .content { position: absolute; left: 14px; right: 14px; top: 42px; }
  .content .body + .sub { margin-top: 8px; }

  /* footer */
  .foot { position: absolute; left: 14px; right: 14px; bottom: 9px; height: 6px;
    border-top: 1px solid var(--rule); display: flex; justify-content: flex-end; gap: 3px; padding-top: 3px; }
  .foot i { display: block; width: 5px; height: 5px; }
  .foot .r { background: var(--red); } .foot .b { background: var(--blue); } .foot .y { background: var(--yellow); }

  /* cover */
  .cover .brand { position: absolute; left: 24px; top: 62px; }
  .cover .brand-mark { width: 26px; height: 26px; }
  .cover .brand-name { font-size: 26px; }
  .cover .band { position: absolute; left: 0; right: 0; top: 150px; height: 62px;
    background: linear-gradient(180deg, var(--red), var(--red-dark)); color: #fff; padding: 12px 24px; }
  .cover .band::after { content: ""; position: absolute; left: 0; right: 0; bottom: -4px; height: 3px; background: var(--blue); }
  .cover .band h1 { font-size: 15px; font-weight: 800; }
  .cover .band p { font-size: 8px; margin-top: 2px; }

  /* chart */
  .chart-area { position: absolute; left: 14px; top: 104px; width: 220px; }
  .bar-row { display: flex; align-items: center; height: 17px; border-bottom: 1px solid var(--rule); }
  .bar-row span { width: 28px; font-size: 6.5px; color: var(--muted); }
  .bar-row b { height: 6px; background: var(--red); display: block; }
  .side-bullets { position: absolute; left: 248px; top: 110px; width: 100px; list-style: none; }
  .side-bullets li { font-size: 6.5px; line-height: 1.45; color: var(--muted); padding-left: 9px; position: relative; margin-bottom: 10px; }
  .side-bullets li::before { content: ""; position: absolute; left: 0; top: 3px; width: 5px; height: 5px; background: var(--red); }

  /* photo */
  .photo { position: absolute; left: 14px; top: 108px; width: 160px; height: 128px;
    background: linear-gradient(160deg, #c9dbea 0%, #8fb2cf 55%, #5c7f9c 100%); }
  .photo-text { position: absolute; left: 184px; top: 108px; right: 14px; }

  /* table */
  .data-table { position: absolute; left: 14px; top: 46px; width: 160px; border-collapse: collapse; }
  .data-table th { background: var(--red); color: #fff; font-size: 6.5px; text-align: left; padding: 4px; }
  .data-table td { font-size: 6.5px; color: var(--muted); padding: 7px 4px; border-bottom: 1px solid var(--rule); }
  .data-table td.pct { width: 34px; border-left: 1px solid var(--rule); text-align: center; }
  .data-table tr:nth-child(even) td { background: #f4f4f4; }
  .icon-list { position: absolute; left: 188px; top: 52px; right: 14px; list-style: none; }
  .icon-list li { display: flex; gap: 7px; align-items: flex-start; margin-bottom: 14px; font-size: 6.5px; line-height: 1.45; color: var(--muted); }
  .icon-list svg { flex: none; }

  /* closing */
  .closing { background: linear-gradient(180deg, var(--red), var(--red-dark)); }
  .closing .thanks { position: absolute; left: 0; right: 0; top: 40px; text-align: center; color: #fff; }
  .closing .thanks h2 { font-size: 13px; font-weight: 800; font-style: italic; }
  .closing .thanks p { font-size: 10px; font-weight: 700; font-style: italic; margin-top: 3px; }
  .closing .brand { position: absolute; left: 0; right: 0; top: 166px; justify-content: center; }
  .closing .brand-mark { width: 24px; height: 24px; background: #fff; }
  .closing .brand-name { font-size: 24px; color: #fff; }
</style>
</head>
<body>

<section class="slide cover row-1 col-1">
  <div class="brand"><span class="brand-mark"></span><span class="brand-name">Craft Harbor</span></div>
  <div class="band">
    <h1>PRESENTATION TITLE</h1>
    <p>Description</p>
  </div>
  <div class="foot"><i class="r"></i><i class="b"></i><i class="y"></i></div>
</section>

<section class="slide row-1 col-2">
  <header class="slide-head">
    <h2 class="slide-title">Presentation Slide Title</h2>
    <div class="brand small"><span class="brand-mark"></span><span class="brand-name">Craft Harbor</span></div>
  </header>
  <div class="content">
    <p class="body">Lorem ipsum dolor sit amet, consectetur adipisicing elit, sed do eiusmod tempor incididunt ut labore et dolore magna aliqua. Ut enim ad minim veniam, quis nostrud exercitation.</p>
    <h3 class="sub">Lorem Ipsum Dolor</h3>
    <p class="body">Duis aute irure dolor in reprehenderit in voluptate velit esse cillum dolore eu fugiat nulla pariatur. Excepteur sint occaecat cupidatat non proident.</p>
    <h3 class="sub">Lorem Ipsum Dolor</h3>
    <p class="body">Duis aute irure dolor in reprehenderit in voluptate velit esse cillum dolore eu fugiat nulla pariatur. Excepteur sint occaecat cupidatat non proident.</p>
  </div>
  <div class="foot"><i class="r"></i><i class="b"></i><i class="y"></i></div>
</section>

<section class="slide row-1 col-3">
  <header class="slide-head">
    <h2 class="slide-title">Presentation Slide Title</h2>
    <div class="brand small"><span class="brand-mark"></span><span class="brand-name">Craft Harbor</span></div>
  </header>
  <div class="content">
    <h3 class="sub">Lorem Ipsum Dolor</h3>
    <p class="body">Duis aute irure dolor in reprehenderit in voluptate velit esse cillum dolore eu fugiat nulla pariatur. Excepteur sint occaecat cupidatat non proident.</p>
  </div>
  <div class="chart-area">
    <div class="bar-row"><span>1990</span><b style="width:60px"></b></div>
    <div class="bar-row"><span>1995</span><b style="width:170px"></b></div>
    <div class="bar-row"><span>2000</span><b style="width:150px"></b></div>
    <div class="bar-row"><span>2005</span><b style="width:185px"></b></div>
    <div class="bar-row"><span>2010</span><b style="width:120px"></b></div>
    <div class="bar-row"><span>2011</span><b style="width:135px"></b></div>
  </div>
  <ul class="side-bullets">
    <li>Duis aute irure dolor in reprehenderit</li>
    <li>Excepteur sint occaecat cupidatat non proident</li>
  </ul>
  <div class="foot"><i class="r"></i><i class="b"></i><i class="y"></i></div>
</section>

<section class="slide row-2 col-1">
  <header class="slide-head">
    <h2 class="slide-title">Presentation Slide Title</h2>
    <div class="brand small"><span class="brand-mark"></span><span class="brand-name">Craft Harbor</span></div>
  </header>
  <div class="content">
    <h3 class="sub">Lorem Ipsum Dolor</h3>
    <p class="body">Duis aute irure dolor in reprehenderit in voluptate velit esse cillum dolore eu fugiat nulla pariatur. Excepteur sint occaecat cupidatat non proident.</p>
  </div>
  <div class="photo" role="img" aria-label="Photo of two engineers in hard hats on a building site under a blue sky"></div>
  <p class="body photo-text">Lorem ipsum dolor sit amet, consectetur adipisicing elit, sed do eiusmod tempor incididunt ut labore et dolore magna aliqua. Ut enim ad minim veniam, quis nostrud exercitation.</p>
  <div class="foot"><i class="r"></i><i class="b"></i><i class="y"></i></div>
</section>

<section class="slide row-2 col-2">
  <header class="slide-head">
    <h2 class="slide-title">Presentation Slide Title</h2>
    <div class="brand small"><span class="brand-mark"></span><span class="brand-name">Craft Harbor</span></div>
  </header>
  <table class="data-table">
    <tr><th colspan="2">Lorem Ipsum Dolor</th></tr>
    <tr><td>Lorem ipsum dolor sit amet</td><td class="pct">10%</td></tr>
    <tr><td>Lorem ipsum dolor sit amet</td><td class="pct">10%</td></tr>
    <tr><td>Lorem ipsum dolor sit amet</td><td class="pct">40%</td></tr>
    <tr><td>Lorem ipsum dolor sit amet</td><td class="pct">30%</td></tr>
    <tr><td>Lorem ipsum dolor sit amet</td><td class="pct">100%</td></tr>
  </table>
  <ul class="icon-list">
    <li><svg width="12" height="12" viewBox="0 0 12 12"><circle cx="6" cy="6" r="6" fill="#c8102e"/><path d="M3.3 6.2l1.8 1.8 3.6-3.8" stroke="#fff" stroke-width="1.4" fill="none"/></svg><span>Lorem ipsum dolor sit amet, consectetur</span></li>
    <li><svg width="12" height="12" viewBox="0 0 12 12"><circle cx="6" cy="6" r="6" fill="#1b75bb"/><path d="M3.3 6.2l1.8 1.8 3.6-3.8" stroke="#fff" stroke-width="1.4" fill="none"/></svg><span>Lorem ipsum dolor sit amet, consectetur</span></li>
    <li><svg width="12" height="12" viewBox="0 0 12 12"><circle cx="6" cy="6" r="6" fill="#f2b705"/><path d="M3.3 6.2l1.8 1.8 3.6-3.8" stroke="#fff" stroke-width="1.4" fill="none"/></svg><span>Lorem ipsum dolor sit amet, consectetur</span></li>
    <li><svg width="12" height="12" viewBox="0 0 12 12"><circle cx="6" cy="6" r="6" fill="#333333"/><path d="M3.3 6.2l1.8 1.8 3.6-3.8" stroke="#fff" stroke-width="1.4" fill="none"/></svg><span>Lorem ipsum dolor sit amet, consectetur</span></li>
  </ul>
  <div class="foot"><i class="r"></i><i class="b"></i><i class="y"></i></div>
</section>

<section class="slide closing row-2 col-3">
  <div class="thanks">
    <h2>THANK YOU FOR YOUR TIME</h2>
    <p>Presentor Name</p>
  </div>
  <div class="brand"><span class="brand-mark"></span><span class="brand-name">Craft Harbor</span></div>
</section>

</body>
</html>
```